Business Card Design Project

We recently redesigned our corporate logo and are looking for a business card refreshment.

The business card template should have a place for the following:
Name, Title, email, phone number, instant messenger handle, and the vitals of the company such as the address, main line, web site etc.

PLEASE DO NOT USE OUR EXISTING WEB SITE FOR INSPIRATION as we are redesigning it.

We've attached a picture of our existing business card as an example, although please keep in mind that we have changed the logo (also attached) and encourage your creativity.

Target Market(s)

Information scientists, search professionals, technical people, Ph.Ds, and executives

Industry/Entity Type

Business

Requirements
Must have
• We'll need the template in a format like Illustrator.

```html
<!DOCTYPE html>
<html lang="en">
<head>
<meta charset="utf-8">
<title>HelixSeek Business Card</title>
<link href="https://fonts.googleapis.com/css2?family=Nunito+Sans:wght@400;600;800&display=swap" rel="stylesheet">
<style>
  :root {
    --stage: #4a3526;
    --card: #ffffff;
    --card-shade: #ececec;
    --blue: #0a86bd;
    --slate: #535c5c;
    --faint: #e3e3e3;
    --ink-light: #dff1f9;
  }
  html, body { margin: 0; height: 100%; overflow: hidden; }
  body {
    width: 1200px; height: 900px; background: var(--stage);
    font-family: "Nunito Sans", sans-serif; position: relative;
  }
  .card {
    position: absolute; left: 250px; width: 700px; height: 400px;
    background: linear-gradient(135deg, var(--card) 40%, var(--card-shade));
    overflow: hidden; box-shadow: 0 10px 30px rgba(0,0,0,.45);
  }
  .card--front { top: 35px; }
  .card--back { top: 465px; }

  .wordmark {
    position: absolute; display: flex; align-items: center; gap: 8px;
    font-weight: 800; color: var(--blue); letter-spacing: .2px;
  }
  .wordmark__dot { width: 22px; height: 22px; border-radius: 50%; background: var(--blue); }

  /* front */
  .front__ring {
    position: absolute; left: 70px; top: 70px; width: 120px; height: 120px;
    border: 28px solid var(--blue); border-radius: 50%;
  }
  .front__bar {
    position: absolute; left: 0; top: 290px; width: 390px; height: 30px; background: var(--blue);
  }
  .front__tab {
    position: absolute; right: 0; top: 90px; width: 150px; height: 28px; background: var(--slate);
  }
  .card--front .wordmark { left: 400px; top: 215px; font-size: 34px; }
  .card--front .wordmark__dot { width: 26px; height: 26px; }

  /* back */
  .card--back .wordmark { right: 40px; top: 40px; font-size: 30px; }
  .back__namebar {
    position: absolute; left: 0; top: 160px; width: 300px; height: 36px; background: var(--slate);
  }
  .back__name {
    position: absolute; left: 100px; top: 163px; margin: 0;
    font-size: 24px; font-weight: 400; color: #fff;
  }
  .back__title {
    position: absolute; left: 100px; top: 200px; margin: 0;
    font-size: 17px; color: var(--blue);
  }
  .back__mark {
    position: absolute; left: 110px; top: 260px; width: 110px; height: 110px;
    border: 26px solid var(--faint); border-radius: 50%;
  }
  .back__panel {
    position: absolute; left: 330px; top: 200px; width: 370px; height: 175px;
    background: var(--blue); color: var(--ink-light); font-size: 13px;
  }
  .contact-col {
    position: absolute; top: 18px; margin: 0; padding: 0 0 0 14px; list-style: none;
    border-left: 1px solid rgba(255,255,255,.55);
  }
  .contact-col--phones { left: 20px; }
  .contact-col--online { left: 185px; }
  .contact-col li { display: flex; align-items: center; gap: 8px; height: 32px; }
  .contact-col svg { width: 14px; height: 14px; fill: none; stroke: var(--ink-light); stroke-width: 1.6; }
  .contact__address { position: absolute; left: 34px; bottom: 14px; margin: 0; font-size: 13px; }
</style>
</head>
<body>
  <section class="card card--front">
    <div class="front__ring"></div>
    <div class="front__bar"></div>
    <div class="front__tab"></div>
    <div class="wordmark"><span class="wordmark__dot"></span>HelixSeek</div>
  </section>

  <section class="card card--back">
    <div class="wordmark"><span class="wordmark__dot"></span>HelixSeek</div>
    <div class="back__namebar"></div>
    <h1 class="back__name">Martin Hale</h1>
    <p class="back__title">General manager</p>
    <div class="back__mark"></div>

    <div class="back__panel">
      <ul class="contact-col contact-col--phones">
        <li><svg viewBox="0 0 14 14"><rect x="3.5" y="1" width="7" height="12" rx="1.5"/></svg>00987654</li>
        <li><svg viewBox="0 0 14 14"><circle cx="7" cy="7" r="6"/><path d="M4.5 4.5c0 3 2 5 5 5"/></svg>222333445</li>
        <li><svg viewBox="0 0 14 14"><rect x="1" y="6" width="12" height="6"/><rect x="3.5" y="1.5" width="7" height="4.5"/></svg>222333445</li>
      </ul>
      <ul class="contact-col contact-col--online">
        <li><svg viewBox="0 0 14 14"><circle cx="7" cy="7" r="2.5"/><path d="M9.5 7v1.5c0 1.5 3 1.5 3-1.5A5.5 5.5 0 1 0 10 11.5"/></svg>hale@helixseek.com</li>
        <li><svg viewBox="0 0 14 14"><path d="M1.5 7 7 2l5.5 5M3 6v6h8V6"/></svg>www.helixseek.com</li>
        <li><svg viewBox="0 0 14 14"><rect x="1.5" y="1.5" width="11" height="11" rx="2"/></svg>martin.hale</li>
      </ul>
      <p class="contact__address">480 Birch Hill Road, Suite 120 Easton, MA 02356</p>
    </div>
  </section>
</body>
</html>
```